Broschüren-Design für studentischen Personaldienstleister
Gute Ideen, reibungslose Zusammenarbeit und alle Anpassungen wurden schnell umgesetzt. Besser konnte es für uns nicht laufen.
Zielgruppe
KL Talentwerk ist ein studentischer Personaldienstleister, der seit 25 Jahren die IT- und Medien-Branche im Contentmanagement (Contentpflege, Redaktion, Grafik) und Onsiteservice (Floorwalking, Help Desk und Service Points) unterstützt.
Hierbei können wir auf das Know-how unserer Studenten vertrauen, die sich in der digitalen Landschaft zu Hause fühlen. Mit ihnen ergänzen wir bestehende Teams, wenn die eigene Crew ausgelastet ist oder keiner der internen Mitarbeiter Fachkenntnisse in dem erforderlichen Bereich mitbringt.
Zu unsere Kunden zählen insbesondere das Verlagswesen (Bsp. Helmut-Fasold SE), Digitalagenturen (Bsp. VORA) und IT-Dienstleister (z.B Rechnorama AG).
Aufgabenstellung
Es soll ein 3-seitiges PDF/ erstellt werden, das NUR ONLINE versendet wird, es wird nicht gedruckt. Das Format kann frei gewählt werden, es soll modern und kreativ sein.
Zusätzlich soll ein Logo/Button entworfen werden, das auf allen Kanälen ausgespielt werden kann (jpg, png und eps.)
Für das 25-jährige-Jubiläum der Zusammenarbeit der Geschäftsführer, Gernot Wallrath und Udo Kestermann, soll ein Mailing an Bestandskunden von KL Talentwerk versendet werden. Diesem Mailing soll ein PDF-Dokument/Flyer angehängt werden. Thematisch wird im Flyer der Claim “Smart. Digital. Im Team.” umgesetzt. Zusätzlich soll das bereits vorhandene Firmenlogo ein eigenes “Jubiläumsbranding” bekommen. Dieses Logo/Button soll sowohl im PDF eingebaut werden als auch zur weiteren thematischen Nutzung auf diversen sozialen Kanälen eingesetzt werden können.
SPEZIFIKATION PDF:
Umfang: 3 Seiten
Format: Kann offen gestaltet werden. Keine Vorgabe.
Inhalt: Die 3 Seiten spiegeln unseren Claim wieder. Auf jeder Seite soll ein „Fun Facts-Kasten“ eingebaut werden, der thematisch auflockert.
Design: Bitte verwenden sie unsere CI-Farben des Logos (HKS 44 + 50% Schwarz und HKS 92K). Logo fügen wir hier ein, Bild- und Textmaterial wird von uns gestellt und nach Zuschlag dem Gewinner zugesendet für die Fertigstellung des PDFs.
Seite 1: IM TEAM
Hier geht chronologisch um die Zusammenarbeit und Entstehung von KL Talentwerk GmbH. Kennenlerngeschichte. Start der Firma in Lüneburg. Zweites Büro in Berlin., neues CEO-Team mit drittem Geschäftsführer, KL Talentwerk heute.
Seite 2: SMART
Smart steht für unsere Studierenden. Warum wir mit studentischen Teams überzeugen. Wir liefern eine Win-Win-Situation mit fairen Konditionen für beide Situationen.
Feedback von unseren Studierenden. Beispiel für eine Erfolgsgeschichte, vom Studenten bei KL Talentwerk GmbH zur leitenden Position bei einem bekannten Medienunternehmen.
S..

```html
<!DOCTYPE html>
<html lang="de">
<head>
<meta charset="utf-8">
<title>KL Talentwerk – Broschüre Innenseiten</title>
<link href="https://fonts.googleapis.com/css2?family=Open+Sans:ital,wght@0,400;0,600;0,700;1,400&family=Ubuntu:wght@500;700&display=swap" rel="stylesheet">
<style>
  :root {
    --brand-blue: #0b4a86;
    --brand-gray: #6c6d70;
    --ring-gray: #8a8b8e;
    --paper: #f4f5f6;
    --backdrop: #e4e6e9;
    --ink: #3d3f44;
    --white: #ffffff;
  }
  * { box-sizing: border-box; margin: 0; padding: 0; }
  html, body { width: 1200px; height: 800px; overflow: hidden; background: var(--backdrop); }
  body { font-family: "Open Sans", sans-serif; color: var(--ink); }

  .spread {
    position: absolute; left: 40px; top: 40px;
    width: 1120px; height: 720px;
    display: flex;
    box-shadow: 0 10px 30px rgba(0,0,0,.12);
  }
  .page {
    position: relative; width: 560px; height: 720px;
    background: var(--paper); overflow: hidden;
  }
  .page--left { border-right: 1px solid #d9dbde; }
  .page-art { position: absolute; inset: 0; }

  .heading {
    font-family: "Ubuntu", sans-serif; font-weight: 700;
    text-transform: uppercase; letter-spacing: .02em;
  }

  /* Left page: story */
  .story { position: absolute; left: 36px; top: 58px; width: 440px; color: var(--white); }
  .story .heading { font-size: 20px; margin-bottom: 16px; }
  .story p { font-size: 11.5px; line-height: 1.5; margin-bottom: 10px; }
  .story strong { font-weight: 700; }

  .team { position: absolute; left: 0; top: 556px; width: 560px; display: flex; justify-content: space-around; padding: 0 20px; }
  .member { width: 160px; margin: 0; text-align: center; }
  .member .avatar { width: 104px; height: 104px; margin: 0 auto 8px; display: block; }
  .member .name { font-family: "Ubuntu", sans-serif; font-weight: 700; font-size: 14px; color: var(--brand-blue); text-transform: uppercase; line-height: 1.3; }
  .member .role { font-family: "Ubuntu", sans-serif; font-weight: 500; font-size: 11.5px; color: var(--brand-gray); text-transform: uppercase; line-height: 1.3; }

  /* Right page: competencies */
  .competencies-title { position: absolute; left: 30px; top: 40px; font-size: 19px; color: var(--brand-blue); }
  .competence { position: absolute; width: 250px; display: flex; gap: 10px; }
  .competence .icon { flex: 0 0 40px; width: 40px; height: 40px; margin-top: 18px; }
  .competence .heading { font-size: 13px; color: var(--brand-blue); margin-bottom: 5px; }
  .competence p { font-size: 10px; line-height: 1.45; color: var(--ink); margin-bottom: 8px; }
  .competence ul { list-style: none; }
  .competence li { font-size: 10.5px; color: var(--brand-blue); font-weight: 600; line-height: 1.5; }
  .competence li::before { content: "▸ "; }
  .competence--content { left: 24px; top: 90px; }
  .competence--onsite { left: 296px; top: 80px; }
  .competence--web { left: 24px; top: 240px; }
  .competence--creative { left: 296px; top: 230px; }

  .testimonials { position: absolute; left: 256px; top: 506px; width: 288px; color: var(--white); }
  .quote { margin-bottom: 10px; }
  .quote .mark { font-family: "Ubuntu", sans-serif; font-weight: 700; font-size: 30px; line-height: .8; height: 16px; display: block; }
  .quote p { font-size: 10px; line-height: 1.4; margin-bottom: 4px; }
  .quote cite { font-style: normal; font-size: 9.5px; text-transform: uppercase; display: block; line-height: 1.35; }
  .quote cite span { text-transform: none; }
</style>
</head>
<body>
<main class="spread">

  <section class="page page--left">
    <svg class="page-art" width="560" height="720" viewBox="0 0 560 720" aria-hidden="true">
      <circle cx="200" cy="-80" r="505" fill="none" stroke="var(--ring-gray)" stroke-width="4"/>
      <circle cx="200" cy="-80" r="480" fill="var(--brand-blue)"/>
      <circle cx="72" cy="405" r="14" fill="var(--brand-blue)"/>
      <circle cx="516" cy="150" r="13" fill="var(--brand-blue)"/>
      <circle cx="300" cy="395" r="150" fill="var(--brand-gray)"/>
    </svg>
    <svg class="page-art" width="560" height="720" viewBox="0 0 560 720" role="img" aria-label="Foto: bunte Handtücher hängen an einer Leine">
      <defs>
        <linearGradient id="towels" x1="0" y1="0" x2="1" y2="0">
          <stop offset="0" stop-color="#6f8a6e"/>
          <stop offset=".4" stop-color="#b9a998"/>
          <stop offset=".7" stop-color="#8d8e90"/>
          <stop offset="1" stop-color="#b8bec6"/>
        </linearGradient>
      </defs>
      <circle cx="300" cy="395" r="135" fill="url(#towels)"/>
    </svg>

    <div class="story">
      <h2 class="heading">So ging's los mit KL Talentwerk</h2>
      <p>Alles begann nach einem Doppelkopfspiel in einer Lüneburger Studentenbude, 1996, als Techno noch cool war.</p>
      <p>Die damaligen BWL- und Medieninformatik-Studenten, Udo und Gernot, hatten nicht nur ihr norddeutsches Gemüt gemeinsam. Sie verband auch der Wunsch, sich beruflich und persönlich vielen Herausforderungen zu stellen.</p>
      <p><strong>Eine davon:</strong> Kunden glücklich machen! Das geht am besten mit einem tollen Team.</p>
    </div>

    <div class="team">
      <figure class="member">
        <svg class="avatar" viewBox="0 0 116 116" role="img" aria-label="Porträtfoto Udo Kestermann">
          <circle cx="58" cy="58" r="54" fill="none" stroke="var(--ring-gray)" stroke-width="1.5"/>
          <circle cx="58" cy="58" r="46" fill="var(--brand-blue)"/>
          <circle cx="58" cy="58" r="41" fill="#c9a98c"/>
          <circle cx="10" cy="84" r="4" fill="var(--brand-blue)"/>
          <circle cx="108" cy="40" r="3.5" fill="var(--brand-blue)"/>
        </svg>
        <figcaption><div class="name">Udo Kestermann</div><div class="role">Geschäftsführer &amp;<br>Gesellschafter</div></figcaption>
      </figure>
      <figure class="member">
        <svg class="avatar" viewBox="0 0 116 116" role="img" aria-label="Porträtfoto Gernot Wallrath">
          <circle cx="58" cy="58" r="54" fill="none" stroke="var(--ring-gray)" stroke-width="1.5"/>
          <circle cx="58" cy="58" r="46" fill="var(--brand-blue)"/>
          <circle cx="58" cy="58" r="41" fill="#a99586"/>
          <circle cx="12" cy="80" r="4" fill="var(--brand-blue)"/>
          <circle cx="106" cy="36" r="3.5" fill="var(--brand-blue)"/>
        </svg>
        <figcaption><div class="name">Gernot Wallrath</div><div class="role">Geschäftsführer &amp;<br>Gesellschafter</div></figcaption>
      </figure>
      <figure class="member">
        <svg class="avatar" viewBox="0 0 116 116" role="img" aria-label="Porträtfoto Malte Brinckhoff">
          <circle cx="58" cy="58" r="54" fill="none" stroke="var(--ring-gray)" stroke-width="1.5"/>
          <circle cx="58" cy="58" r="46" fill="var(--brand-blue)"/>
          <circle cx="58" cy="58" r="41" fill="#8f8780"/>
          <circle cx="14" cy="86" r="4" fill="var(--brand-blue)"/>
          <circle cx="108" cy="50" r="3.5" fill="var(--brand-blue)"/>
        </svg>
        <figcaption><div class="name">Malte Brinckhoff</div><div class="role">Geschäftsführer &amp;<br>Gesellschafter</div></figcaption>
      </figure>
    </div>
  </section>

  <section class="page page--right">
    <svg class="page-art" width="560" height="720" viewBox="0 0 560 720" aria-hidden="true">
      <circle cx="150" cy="820" r="240" fill="var(--brand-gray)"/>
      <circle cx="470" cy="720" r="316" fill="none" stroke="var(--ring-gray)" stroke-width="3"/>
      <circle cx="470" cy="720" r="300" fill="var(--brand-blue)"/>
      <circle cx="205" cy="573" r="9" fill="var(--brand-blue)"/>
      <circle cx="380" cy="418" r="9" fill="var(--brand-blue)"/>
    </svg>

    <h2 class="heading competencies-title">These are our core competencies</h2>

    <article class="competence competence--content">
      <svg class="icon" viewBox="0 0 40 40" aria-hidden="true">
        <circle cx="20" cy="20" r="20" fill="var(--brand-blue)"/>
        <rect x="11" y="12" width="18" height="13" rx="1.5" fill="none" stroke="#fff" stroke-width="1.6"/>
        <path d="M14 17h12M14 21h8" stroke="#fff" stroke-width="1.4"/>
        <path d="M16 29h8" stroke="#fff" stroke-width="1.6"/>
      </svg>
      <div>
        <h3 class="heading">Contentmanagement</h3>
        <p>Ob ein kompletter Portalaufbau oder reine Datenmigration, wir unterstützen Sie flexibel in allen Bereichen rund ums Contentmanagement.</p>
        <ul><li>Datenmigration</li><li>Redaktioneller Support</li><li>Suchmaschinenoptimierung (SEO)</li></ul>
      </div>
    </article>

    <article class="competence competence--onsite">
      <svg class="icon" viewBox="0 0 40 40" aria-hidden="true">
        <circle cx="20" cy="20" r="20" fill="var(--brand-blue)"/>
        <circle cx="20" cy="20" r="9" fill="none" stroke="#fff" stroke-width="1.6"/>
        <ellipse cx="20" cy="20" rx="4" ry="9" fill="none" stroke="#fff" stroke-width="1.4"/>
        <path d="M11 20h18" stroke="#fff" stroke-width="1.4"/>
      </svg>
      <div>
        <h3 class="heading">On-Site-Services</h3>
        <p>In der digital wachsenden Welt fallen neue Apps und Tools praktisch über Nacht vom Himmel und wollen richtig bedient werden.</p>
        <ul><li>First-Level-Support</li><li>Floorwalker</li><li>Servicepoint</li></ul>
      </div>
    </article>

    <article class="competence competence--web">
      <svg class="icon" viewBox="0 0 40 40" aria-hidden="true">
        <circle cx="20" cy="20" r="20" fill="var(--brand-blue)"/>
        <rect x="10" y="12" width="20" height="14" rx="1.5" fill="none" stroke="#fff" stroke-width="1.6"/>
        <path d="M17 17l-3 2 3 2M23 17l3 2-3 2" fill="none" stroke="#fff" stroke-width="1.4"/>
        <path d="M16 29h8" stroke="#fff" stroke-width="1.6"/>
      </svg>
      <div>
        <h3 class="heading">Webdevelopment</h3>
        <p>Mobile App- und agile Software-Entwicklung mit Clean Codes schütteln unsere erfahrenen Webdeveloper locker aus dem Ärmel.</p>
        <ul><li>Entwicklung</li><li>Testing &amp; Qualitätssicherung</li></ul>
      </div>
    </article>

    <article class="competence competence--creative">
      <svg class="icon" viewBox="0 0 40 40" aria-hidden="true">
        <circle cx="20" cy="20" r="20" fill="var(--brand-blue)"/>
        <path d="M20 10a7 7 0 0 0-4 12.7V26h8v-3.3A7 7 0 0 0 20 10z" fill="none" stroke="#fff" stroke-width="1.6"/>
        <path d="M17 29h6" stroke="#fff" stroke-width="1.6"/>
      </svg>
      <div>
        <h3 class="heading">Kreativleistungen</h3>
        <p>Unsere studentischen Webdesigner sind fit in HTML, HTML5, CSS und CSS3 und haben ein Auge dafür, im Sinne Ihrer Markenidentität interaktive, ästhetisch ansprechende Webdesigns zu kreieren.</p>
        <ul><li>Grafik &amp; Layout</li><li>Advertorials</li></ul>
      </div>
    </article>

    <div class="testimonials">
      <blockquote class="quote">
        <span class="mark">“</span>
        <p>Ich wünsche mir, dass wir weiterhin so gut zusammenarbeiten wie bisher – von mir aus auch noch intensiver</p>
        <cite>Cordavia<br><span>Senior IT-Consultant</span></cite>
      </blockquote>
      <blockquote class="quote">
        <span class="mark">“</span>
        <p>Ich wollte mich nochmal ganz herzlich für Eure Unterstützung und vor allem für Eure Flexibilität bedanken!!! Ohne Euch und Euer Team wäre es nicht so ein Erfolg geworden. Großes Lob an alle Beteiligten für Ihr Engagement und ich freue mich auf’s nächste Mal.</p>
        <cite>Tageskurier.de<br><span>Head of Product Development</span></cite>
      </blockquote>
    </div>
  </section>

</main>
</body>
</html>
```